Pillow Company needs Pillow Insert Design

I just started a new pillow line with two pillow types. I have a hotel pillow and an organic pillow. I need two pillow insert signs designed that follow the same layout but are different color types. I want one sign to incorporate silver and white look and another sign to incorporate a green and white look (this one to look organic). They must have the same layout but different colors. I have include examples of what I want it to look like. In addition, I have uploaded the two hi res images for each sign. My logo is uploaded too.

I am open to other concepts and colors as long as it looks modern, clean and upscale. In addition, I need a Made in the USA logo on the pillow insert designs.

I have attached details on sign, images to be used, and examples that I like.

The Pillow Sign Size is 12 inches x 12 inches.

```html
<!DOCTYPE html>
<html lang="en">
<head>
<meta charset="utf-8">
<title>NestLeaf Luxurious Pillow Insert</title>
<link href="https://fonts.googleapis.com/css2?family=Open+Sans:wght@400;600;700&family=Pinyon+Script&display=swap" rel="stylesheet">
<style>
  :root {
    --page: #ffffff;
    --brand-green: #1f7a3a;
    --leaf-green: #7cc242;
    --script-green: #1d5e2c;
    --panel-light: #8a8a8a;
    --panel-mid: #b3b3b3;
    --panel-dark: #1b1b1b;
    --text-light: #ffffff;
    --text-dark: #2a2a2a;
    --silver-a: #ffffff;
    --silver-b: #c9cacc;
    --photo-a: #e9e4df;
    --photo-b: #cfc7bf;
    --badge-blue: #1d3f8f;
    --badge-red: #c8202f;
  }
  * { box-sizing: border-box; margin: 0; padding: 0; }
  html, body { width: 1200px; height: 1000px; overflow: hidden; background: var(--page); }
  .insert { position: relative; width: 1200px; height: 1000px; font-family: "Open Sans", Arial, sans-serif; }

  .silver-band {
    position: absolute; left: 690px; top: 64px; width: 345px; height: 126px;
    background: linear-gradient(90deg, var(--silver-a), var(--silver-b));
  }
  .brand {
    position: absolute; left: 215px; top: 88px; height: 62px;
    display: flex; align-items: center; gap: 16px;
  }
  .brand-square { width: 62px; height: 62px; background: var(--leaf-green); border-radius: 6px; }
  .brand-name { font-weight: 600; font-size: 42px; color: var(--brand-green); letter-spacing: -0.5px; }

  .lifestyle-photo {
    position: absolute; left: 505px; top: 190px; width: 530px; height: 470px;
    background:
      linear-gradient(180deg, rgba(255,255,255,0) 55%, #ffffff 100%),
      linear-gradient(120deg, var(--photo-b) 0%, var(--photo-a) 45%, #f6f4f2 100%);
  }

  .info-panel { position: absolute; left: 163px; top: 190px; width: 342px; height: 745px; }
  .panel-intro {
    position: absolute; left: 0; top: 0; width: 342px; height: 298px;
    background: linear-gradient(180deg, var(--panel-mid) 0%, #9a9a9a 40%, var(--panel-light) 100%);
  }
  .panel-features-copy {
    position: absolute; left: 0; top: 298px; width: 342px; height: 148px;
    background: linear-gradient(180deg, #b5b5b5, #9c9c9c);
  }
  .panel-list {
    position: absolute; left: 0; top: 446px; width: 342px; height: 299px;
    background: linear-gradient(180deg, #5a5a5a 0%, #2e2e2e 55%, var(--panel-dark) 100%);
  }

  .title-script {
    position: absolute; font-family: "Pinyon Script", cursive; color: var(--text-light);
    text-shadow: 0 2px 6px rgba(0,0,0,0.35); line-height: 1;
  }
  .title-first { left: 186px; top: 205px; font-size: 92px; }
  .title-second { left: 318px; top: 282px; font-size: 92px; }

  .intro-copy {
    position: absolute; left: 180px; top: 383px; width: 320px;
    color: var(--text-light); font-weight: 700; font-size: 13.6px; line-height: 19.5px;
    letter-spacing: 0.6px; text-transform: uppercase;
  }
  .features-copy {
    position: absolute; left: 170px; top: 500px; width: 330px; text-align: center;
    color: var(--text-light); font-weight: 600; font-size: 13.4px; line-height: 20px;
  }
  .benefit-list { position: absolute; left: 186px; top: 666px; list-style: none; }
  .benefit-list li {
    position: relative; padding-left: 23px; color: var(--text-light);
    font-weight: 600; font-size: 12.6px; line-height: 25.2px;
  }
  .benefit-list li .bullet { position: absolute; left: 0; top: 7px; width: 11px; height: 11px; }
  .benefit-list li.indent-follow { padding-left: 23px; }

  .tagline {
    position: absolute; left: 525px; top: 705px; width: 490px;
    font-family: "Pinyon Script", cursive; font-size: 50px; color: var(--script-green);
    transform: rotate(-5deg); transform-origin: left center; white-space: nowrap;
  }
  .origin-note {
    position: absolute; left: 640px; top: 855px; width: 208px; text-align: right;
    font-size: 15.5px; line-height: 21px; color: var(--text-dark);
  }
  .origin-badge { position: absolute; left: 856px; top: 768px; width: 140px; height: 140px; }
</style>
</head>
<body>
<main class="insert">
  <div class="silver-band"></div>

  <header class="brand">
    <span class="brand-square"></span>
    <span class="brand-name">NestLeaf</span>
  </header>

  <div class="lifestyle-photo" role="img" aria-label="Photo of a smiling couple relaxing in a white bed with breakfast in the foreground"></div>

  <section class="info-panel">
    <div class="panel-intro"></div>
    <div class="panel-features-copy"></div>
    <div class="panel-list"></div>
  </section>

  <h1 class="title-script title-first">Luxurious</h1>
  <span class="title-script title-second">Pillow</span>

  <p class="intro-copy">This pillow was designed to give you the most comfortable night's sleep in your life. Designed for all types of sleep positions.</p>

  <p class="features-copy">We added revolutionary features from our advanced Super Soft Premium Memory Foam that has an open cell structure design that recovers quickly and does not trap heat to our gel infused polyester fiber to our temperature managing Lyocell Fabric.</p>

  <ul class="benefit-list">
    <li><svg class="bullet" viewBox="0 0 11 11"><rect x="0.5" y="0.5" width="10" height="10" fill="none" stroke="#fff"/><path d="M2.5 2.5L8.5 8.5M8.5 2.5L2.5 8.5" stroke="#fff"/></svg>Made From the Finest Premium Materials</li>
    <li><svg class="bullet" viewBox="0 0 11 11"><rect x="0.5" y="0.5" width="10" height="10" fill="none" stroke="#fff"/><path d="M2.5 2.5L8.5 8.5M8.5 2.5L2.5 8.5" stroke="#fff"/></svg>Adjusts to your Body Weight and Temperature</li>
    <li><svg class="bullet" viewBox="0 0 11 11"><rect x="0.5" y="0.5" width="10" height="10" fill="none" stroke="#fff"/><path d="M2.5 2.5L8.5 8.5M8.5 2.5L2.5 8.5" stroke="#fff"/></svg>Ventilated and Does Not Trap Heat</li>
    <li><svg class="bullet" viewBox="0 0 11 11"><rect x="0.5" y="0.5" width="10" height="10" fill="none" stroke="#fff"/><path d="M2.5 2.5L8.5 8.5M8.5 2.5L2.5 8.5" stroke="#fff"/></svg>Cool Non-Allergenic, Anti-Microbial,</li>
    <li class="indent-follow">and Hypoallergenic</li>
    <li><svg class="bullet" viewBox="0 0 11 11"><rect x="0.5" y="0.5" width="10" height="10" fill="none" stroke="#fff"/><path d="M2.5 2.5L8.5 8.5M8.5 2.5L2.5 8.5" stroke="#fff"/></svg>Conforms to Head and Neck for optimal</li>
    <li class="indent-follow">Alignment during Sleep</li>
    <li><svg class="bullet" viewBox="0 0 11 11"><rect x="0.5" y="0.5" width="10" height="10" fill="none" stroke="#fff"/><path d="M2.5 2.5L8.5 8.5M8.5 2.5L2.5 8.5" stroke="#fff"/></svg>Mildew Proof and Dust Mite Resistant</li>
    <li><svg class="bullet" viewBox="0 0 11 11"><rect x="0.5" y="0.5" width="10" height="10" fill="none" stroke="#fff"/><path d="M2.5 2.5L8.5 8.5M8.5 2.5L2.5 8.5" stroke="#fff"/></svg>PureFoam ® toxin free certified foam</li>
  </ul>

  <p class="tagline">Surround yourself with the Best!</p>

  <p class="origin-note">Individually Handcrafted<br>and Made in USA</p>

  <svg class="origin-badge" viewBox="0 0 140 140" role="img" aria-label="Made in USA badge">
    <circle cx="70" cy="70" r="68" fill="var(--badge-blue)"/>
    <circle cx="70" cy="70" r="50" fill="#ffffff"/>
    <circle cx="70" cy="70" r="44" fill="var(--badge-red)"/>
  </svg>
</main>
</body>
</html>
```